Halvorsen Construction Needs a Business Card

Our current business card is very bland, and since we have a new logo, we would like a new business card design to reflect our company. It can be a single-sided or two-sided card, but it is important that our contact information appears on the same side. I am attaching a copy of our old card and our new logo. If you need the logo in another format than the one I'm sending, please let me know. This is the information that we must have on our card, but not necessarily in any specific order:
1) Our logo
2) General Contractor
3) Dale Halvorsen, Owner
4) 482 Commerce Ridge Road, Ridgeford, Westmark 35871
5) Office: 256-555-0147
7) Fax: 256-555-0148
8) Cell: 256-555-0193
9) halvorsenconstruction@qvl-mail.net
10) halvorsenconstruction-example.com (can be omitted if necessary)
Also, I will need files in a format that I can alter if any of the above information changes in the near future. Thank you in advance for your submissions!
Target Market(s)
Commercial and residential clients, architects, and subcontractors.
Industry/Entity Type
Business
Look and feel

```html
<!DOCTYPE html>
<html lang="en">
<head>
<meta charset="utf-8">
<title>Halvorsen Construction – Business Card</title>
<link rel="stylesheet" href="https://fonts.googleapis.com/css2?family=Roboto+Condensed:wght@400;700&display=swap">
<style>
  :root {
    --backdrop: #f3f1ea;
    --card-white: #ffffff;
    --card-black: #000000;
    --ink: #111111;
    --accent-yellow: #f2c230;
    --faint-grey: #e2e2e2;
  }
  * { margin: 0; padding: 0; box-sizing: border-box; }
  html, body {
    width: 1200px; height: 900px; overflow: hidden;
    background: var(--backdrop);
    font-family: "Roboto Condensed", "Arial Narrow", sans-serif;
    color: var(--ink);
  }
  .sheet {
    width: 1200px; height: 900px;
    display: flex; flex-direction: column;
    align-items: center; justify-content: center; gap: 50px;
  }
  .card {
    position: relative;
    width: 700px; height: 400px;
    box-shadow: 0 2px 10px rgba(0,0,0,0.12);
    overflow: hidden;
  }
  /* Front */
  .card-front { background: var(--card-white); }
  .faint-block {
    position: absolute; left: 380px; top: 40px;
    width: 230px; height: 230px;
    background: var(--faint-grey); opacity: 0.7;
  }
  .owner {
    position: absolute; left: 350px; top: 46px;
  }
  .owner-name { font-size: 30px; font-weight: 700; letter-spacing: 0.5px; }
  .owner-title { font-size: 20px; font-weight: 700; margin-top: 4px; }
  .divider {
    position: absolute; left: 40px; top: 136px;
    width: 620px; height: 2px; background: var(--accent-yellow);
  }
  .brand {
    position: absolute; left: 40px; top: 168px;
    display: flex; align-items: center; gap: 12px;
  }
  .brand-square { width: 44px; height: 44px; background: var(--ink); }
  .brand-name {
    font-size: 22px; font-weight: 700; line-height: 1.05; letter-spacing: 1px;
  }
  .tagline {
    position: absolute; left: 40px; top: 232px;
    font-size: 24px; font-weight: 700;
  }
  .contacts {
    position: absolute; left: 350px; top: 156px;
    font-size: 20px; font-weight: 700; line-height: 1.3;
  }
  .phone-row { display: flex; }
  .phone-label { width: 72px; }
  .online { margin-top: 8px; font-size: 17px; line-height: 1.35; }
  .address {
    position: absolute; left: 0; right: 0; bottom: 36px;
    text-align: center; font-size: 19px; font-weight: 700;
  }
  /* Back */
  .card-back {
    background: var(--card-black);
    display: flex; align-items: center; justify-content: center; gap: 22px;
  }
  .back-square { width: 70px; height: 70px; background: var(--card-white); }
  .back-name {
    color: var(--card-white); font-size: 40px; font-weight: 700;
    letter-spacing: 2px; line-height: 1.05;
  }
</style>
</head>
<body>
<main class="sheet">
  <section class="card card-front" aria-label="Card front">
    <div class="faint-block" aria-hidden="true"></div>
    <div class="owner">
      <p class="owner-name">Dale Halvorsen</p>
      <p class="owner-title">Owner</p>
    </div>
    <div class="divider" aria-hidden="true"></div>
    <div class="brand">
      <div class="brand-square" aria-hidden="true"></div>
      <p class="brand-name">HALVORSEN<br>CONSTRUCTION</p>
    </div>
    <p class="tagline">Licensed General Contractor</p>
    <div class="contacts">
      <p class="phone-row"><span class="phone-label">Office</span><span>: 256-555-0147</span></p>
      <p class="phone-row"><span class="phone-label">Fax</span><span>: 256-555-0148</span></p>
      <p class="phone-row"><span class="phone-label">Cell</span><span>: 256-555-0193</span></p>
      <p class="online">halvorsenconstruction@qvl-mail.net<br>www.halvorsenconstruction-example.com</p>
    </div>
    <p class="address">482 Commerce Ridge Road, Ridgeford, Westmark 35871</p>
  </section>

  <section class="card card-back" aria-label="Card back">
    <div class="back-square" aria-hidden="true"></div>
    <p class="back-name">HALVORSEN<br>CONSTRUCTION</p>
  </section>
</main>
</body>
</html>
```